Create for us a Shop-Stopper Business Card

We need a standout, first class business card to go along with our new brand strategy. Sleek, Contemporary and fresh.

Colors and theme must sync with our websitewww.pelvorpower.co.uk

We want a business card that has a global brand appeal. TKR Energy is a small UK renewable company that specialises in energy projects in Africa. We want a business card that has the following characteristics: Very short, precise, global, stand out, NOT TOO LOUD but contemporary. The company's colour themes are White, Grey with a hint of green.

Target Market(s)

Business exec, high net worth individuals, investors, commercial leaders, suppliers, government officials

Industry/Entity Type

Solar Energy

Contact Information for Business Card

Logo, Name, Title, Address, web address, email,

Requirements
Must have
• Logo must be sharp
Nice to have
• Adapt fonts from the logo. The large circular side of the logo at the back in a very refreshing way
Should not have
• No solar panel shapes or image.Very little black. If possible avoid black. Its not coming out nice. I think !!!

```html
<!DOCTYPE html>
<html lang="en">
<head>
<meta charset="utf-8">
<title>TKR Energy Business Card</title>
<link rel="stylesheet" href="https://fonts.googleapis.com/css2?family=Mulish:wght@400;700&family=Questrial&display=swap">
<style>
  :root {
    --backdrop: #0d0d0d;
    --card-white: #ffffff;
    --ink: #2f2f2f;
    --ink-soft: #3a3a3a;
    --accent-red: #c8102e;
    --leaf-green: #6cbf2c;
    --green-light: #7bc142;
    --green-deep: #1e8c3e;
    --green-band-top: #7cc242;
    --green-band-bottom: #3fa23a;
  }
  * { box-sizing: border-box; margin: 0; padding: 0; }
  html, body {
    width: 1200px; height: 900px; overflow: hidden;
    background: var(--backdrop);
  }
  .canvas { position: relative; width: 1200px; height: 900px; }

  .card {
    position: absolute; top: 306px;
    width: 440px; height: 271px;
    border-radius: 10px; overflow: hidden;
  }
  .card-front { left: 149px; background: var(--card-white); }
  .card-back {
    left: 608px;
    background: linear-gradient(180deg, var(--green-light) 0%, #4eab3d 55%, var(--green-deep) 100%);
  }

  /* front */
  .brand {
    position: absolute; left: 163px; top: 32px;
    display: flex; align-items: center;
  }
  .brand-dot {
    width: 50px; height: 50px; border-radius: 50%;
    background: var(--leaf-green); margin-right: 8px;
  }
  .brand-name {
    font-family: "Questrial", sans-serif;
    font-size: 31px; color: var(--ink);
    letter-spacing: 0.5px; line-height: 1;
  }
  .brand-rule {
    position: absolute; left: 221px; top: 75px;
    width: 198px; height: 2px; background: var(--accent-red);
  }
  .person { position: absolute; left: 29px; top: 132px; font-family: "Mulish", sans-serif; }
  .person-name { font-size: 17px; font-weight: 700; color: var(--leaf-green); line-height: 20px; }
  .person-title { font-size: 12.5px; color: var(--ink-soft); line-height: 16px; }
  .divider {
    position: absolute; left: 0; top: 182px;
    width: 100%; height: 1px; background: var(--accent-red);
  }
  .contacts {
    position: absolute; left: 163px; top: 195px;
    list-style: none; font-family: "Mulish", sans-serif;
    font-size: 13px; color: var(--ink);
  }
  .contacts li { display: flex; align-items: center; height: 16px; }
  .contacts svg { width: 10px; height: 10px; margin-right: 7px; fill: var(--leaf-green); }
  .foot-band {
    position: absolute; left: 0; bottom: 0;
    width: 100%; height: 11px;
    background: linear-gradient(180deg, var(--green-band-top), var(--green-band-bottom));
  }
  .foot-notch {
    position: absolute; left: 159px; bottom: 0;
    width: 12px; height: 13px; background: var(--card-white);
  }

  /* back */
  .back-motif {
    position: absolute; left: 0; top: 20px; width: 300px; height: 251px;
    background: radial-gradient(ellipse at 45% 55%, rgba(255,255,255,0.10), rgba(255,255,255,0) 70%);
  }
  .back-brand {
    position: absolute; left: 0; top: 153px; width: 100%;
    text-align: center;
    font-family: "Questrial", sans-serif;
    font-size: 42px; color: #ffffff; line-height: 1;
    letter-spacing: 0.5px;
  }
  .back-rule {
    position: absolute; left: 89px; top: 197px;
    width: 263px; height: 2px; background: #ffffff;
  }
  .back-address {
    position: absolute; left: 0; top: 211px; width: 100%;
    text-align: center;
    font-family: "Mulish", sans-serif; font-size: 12.5px; color: #ffffff;
  }
</style>
</head>
<body>
<main class="canvas">
  <section class="card card-front">
    <div class="brand">
      <span class="brand-dot"></span>
      <span class="brand-name">TKR ENERGY</span>
    </div>
    <div class="brand-rule"></div>
    <div class="person">
      <p class="person-name">Daniel Hart</p>
      <p class="person-title">Managing Director</p>
    </div>
    <div class="divider"></div>
    <ul class="contacts">
      <li><svg viewBox="0 0 10 10"><path d="M2 0.5 L3.6 2.6 L2.7 3.6 Q3.7 5.8 6.4 7.3 L7.4 6.4 L9.5 8 L8.3 9.5 Q3.5 8.5 0.5 1.7 Z"/></svg>044-987 654 321</li>
      <li><svg viewBox="0 0 10 10"><path d="M0.5 2 H9.5 V8.5 H0.5 Z M0.5 2 L5 5.5 L9.5 2" stroke="#fff" stroke-width="0.8"/></svg>info@tkrenergy.com</li>
      <li><svg viewBox="0 0 10 10"><path d="M1.5 6.5 L3.5 4.5 M4 8 L8 4 A1.6 1.6 0 0 0 6 2 L2 6 A1.6 1.6 0 0 0 4 8 Z" fill="none" stroke="#6cbf2c" stroke-width="1.3"/></svg>www.pelvorpower.co.uk</li>
    </ul>
    <div class="foot-band"></div>
    <div class="foot-notch"></div>
  </section>

  <section class="card card-back">
    <div class="back-motif" role="img" aria-label="Faint large brand emblem decoration"></div>
    <p class="back-brand">TKR ENERGY</p>
    <div class="back-rule"></div>
    <p class="back-address">12345, Address Goes Here Country Name, 123456.</p>
  </section>
</main>
</body>
</html>
```